Pediatric Dental Practice needs a postcard for direct mail advertising

We are looking for a creative and professional double-sided postcard design for a direct mail marketing campaign. Our goal is to attract new families to our pediatric dental practice by conveying a sense of warmth, modern care, and clinical excellence. The design should feel "boutique" and high-end yet remain fun and approachable for parents and children.

```html
<!DOCTYPE html>
<html lang="en">
<head>
<meta charset="utf-8">
<title>Maple Grove Pediatric Dentistry – Postcard</title>
<link href="https://fonts.googleapis.com/css2?family=Lora:wght@500;600&family=Nunito+Sans:wght@400;600;700&display=swap" rel="stylesheet">
<style>
:root{
  --backdrop:#064a52;
  --paper:#f8f5f1;
  --green:#4f8a45;
  --green-soft:#7a9c65;
  --green-pale:#a9c39a;
  --ink:#2e3838;
  --text:#3c4444;
  --line:#8a8f8c;
  --serif:'Lora', Georgia, serif;
  --sans:'Nunito Sans', Arial, sans-serif;
}
*{box-sizing:border-box;margin:0;padding:0}
html,body{width:873px;height:1200px;overflow:hidden;background:var(--backdrop)}
body{position:relative;font-family:var(--sans);color:var(--text)}
.card{position:absolute;background:var(--paper);overflow:hidden;box-shadow:0 6px 18px rgba(0,0,0,.35)}
.card--front{left:76px;top:59px;width:724px;height:505px}
.card--back{left:74px;top:626px;width:725px;height:506px}
.abs{position:absolute}

/* front */
.brand{left:0;width:290px;top:92px;text-align:center}
.brand__row{display:flex;align-items:center;justify-content:center;gap:8px}
.brand__dot{width:20px;height:20px;border-radius:50%;background:var(--green-soft)}
.brand__name{font-family:var(--sans);font-weight:600;font-size:22px;line-height:26px;color:var(--ink);letter-spacing:.3px}
.brand__sub{margin-top:3px;font-size:7.5px;letter-spacing:2.3px;font-weight:700;color:var(--ink)}
.headline{left:41px;top:158px;font-family:var(--serif);font-weight:600;font-size:55px;line-height:56px;color:var(--green);letter-spacing:-.5px}
.headline .dark{color:var(--ink)}
.divider{left:42px;top:339px;width:206px;height:14px}
.values{left:42px;width:206px;top:363px;text-align:center;font-size:12px;line-height:19px;font-weight:700;letter-spacing:.6px;color:var(--green)}
.welcome{left:42px;top:439px;width:206px;height:46px;border-radius:14px;background:var(--green-soft);padding:3px}
.welcome__inner{height:100%;border:1px dashed rgba(255,255,255,.7);border-radius:11px;display:flex;align-items:center;gap:14px;padding-left:18px;color:#fff;font-size:12.5px;line-height:16px;letter-spacing:1.3px;font-weight:600}
.photo{left:0;top:0}
.badge{left:550px;top:351px;width:156px;height:156px;border-radius:50%;background:var(--green-soft);display:flex;align-items:center;justify-content:center}
.badge__ring{position:absolute;inset:6px;border:1px dashed rgba(255,255,255,.75);border-radius:50%}
.badge__text{font-family:var(--serif);font-size:16px;line-height:20px;color:#fff;text-align:center;margin-top:6px}
.badge__text svg{display:block;margin:0 auto 6px}

/* back */
.ages{left:0;width:340px;top:23px;text-align:center;font-size:13.5px;letter-spacing:1.2px;font-weight:700;color:var(--green)}
.ages-divider{left:124px;top:46px;width:92px;height:12px}
.service{display:flex;align-items:center;gap:10px;width:150px}
.service__icon{width:40px;height:40px;border-radius:50%;border:1px solid var(--green-pale);display:flex;align-items:center;justify-content:center;flex:none}
.service__label{font-size:10.5px;line-height:14px;color:var(--ink);font-weight:600}
.offer{left:44px;top:243px;width:252px;height:111px;border-radius:10px;background:var(--green-soft);padding:4px;box-shadow:0 0 0 3px #c8d8bd}
.offer__inner{height:100%;border:1px dashed rgba(255,255,255,.7);border-radius:7px;text-align:center;color:#fff;display:flex;flex-direction:column;align-items:center;justify-content:center}
.offer__amount{font-family:var(--serif);font-weight:600;font-size:44px;line-height:44px}
.offer__amount small{font-size:29px;margin-left:4px}
.offer__line{font-size:12.5px;line-height:16px;letter-spacing:.5px;margin-top:3px}
.offer__note{font-size:9.5px;line-height:12px;letter-spacing:.6px;margin-top:7px}
.offer__notch{left:158px;top:230px;width:24px;height:24px;border-radius:50%;background:var(--paper);display:flex;align-items:center;justify-content:center}
.contact{left:43px;top:374px;font-size:12px;color:var(--ink)}
.contact li{list-style:none;display:flex;align-items:center;gap:10px;height:24px}
.contact svg{flex:none}
.contact .sep{color:#aaa;margin:0 6px}
.rule-v{left:369px;top:21px;width:1px;height:461px;background:#d4d6d0}
.rule-heart{left:360px;top:200px;background:var(--paper);padding:4px 0}
.stamp{left:621px;top:21px;width:69px;height:84px;border:1px solid #555;font-size:11px;line-height:17px;text-align:center;color:var(--ink);padding-top:16px;letter-spacing:.3px}
.address-line{left:419px;width:271px;height:1px;background:var(--line)}
</style>
</head>
<body>

<section class="card card--front">
  <svg class="abs photo" width="724" height="505" role="img" aria-label="Photo of a bright pediatric dental treatment room with a teal patient chair, exam light, window and plush toy">
    <defs>
      <linearGradient id="room" x1="0" y1="0" x2="1" y2="1">
        <stop offset="0" stop-color="#e2e6b8"/>
        <stop offset=".45" stop-color="#c9d9a6"/>
        <stop offset=".7" stop-color="#4fa9a3"/>
        <stop offset="1" stop-color="#d9b784"/>
      </linearGradient>
    </defs>
    <path d="M310 0 C268 80 300 150 298 235 C296 320 258 390 280 505 L724 505 L724 0 Z" fill="url(#room)" stroke="#9dbb8c" stroke-width="3"/>
  </svg>

  <div class="abs brand">
    <div class="brand__row"><span class="brand__dot"></span><span class="brand__name">maple grove</span></div>
    <div class="brand__sub">PEDIATRIC DENTISTRY</div>
  </div>

  <h1 class="abs headline">Healthy<br>smiles<br><span class="dark">grow here.</span></h1>

  <svg class="abs divider" viewBox="0 0 206 14">
    <line x1="0" y1="7" x2="92" y2="7" stroke="#b9c8b0"/>
    <line x1="114" y1="7" x2="206" y2="7" stroke="#b9c8b0"/>
    <path d="M103 12 L97 6 A3 3 0 0 1 103 3 A3 3 0 0 1 109 6 Z" fill="var(--green)"/>
  </svg>

  <p class="abs values">GENTLE CARE.<br>MODERN TECHNOLOGY.<br>MADE FOR KIDS.</p>

  <div class="abs welcome">
    <div class="welcome__inner">
      <svg width="20" height="18" viewBox="0 0 20 18"><path d="M10 17 L2 9 A5 5 0 0 1 10 2.5 A5 5 0 0 1 18 9 Z" fill="#fff"/></svg>
      <span>NOW WELCOMING<br>NEW FAMILIES</span>
    </div>
  </div>

  <div class="abs badge">
    <span class="badge__ring"></span>
    <p class="badge__text">
      <svg width="16" height="14" viewBox="0 0 20 18"><path d="M10 17 L2 9 A5 5 0 0 1 10 2.5 A5 5 0 0 1 18 9 Z" fill="#fff"/></svg>
      Where little<br>smiles feel<br>right at home.
    </p>
  </div>
</section>

<section class="card card--back">
  <h2 class="abs ages">CARE FOR AGES 0 TO TEEN</h2>
  <svg class="abs ages-divider" viewBox="0 0 92 12">
    <line x1="0" y1="6" x2="34" y2="6" stroke="#b9c8b0"/>
    <line x1="58" y1="6" x2="92" y2="6" stroke="#b9c8b0"/>
    <path d="M46 10.5 L41 5.5 A2.6 2.6 0 0 1 46 3 A2.6 2.6 0 0 1 51 5.5 Z" fill="var(--green)"/>
  </svg>

  <div class="abs service" style="left:43px;top:73px">
    <span class="service__icon"><svg width="20" height="22" viewBox="0 0 20 22" fill="none" stroke="var(--green)" stroke-width="1.2"><path d="M5 2 C2 2 1 5 2 9 C3 12 3 20 6 20 C8 20 8 13 10 13 C12 13 12 20 14 20 C17 20 17 12 18 9 C19 5 18 2 15 2 C13 2 12 3 10 3 C8 3 7 2 5 2 Z"/></svg></span>
    <span class="service__label">Preventive<br>Care</span>
  </div>
  <div class="abs service" style="left:183px;top:73px">
    <span class="service__icon"><svg width="20" height="22" viewBox="0 0 20 22" fill="none" stroke="var(--green)" stroke-width="1.2"><path d="M5 2 C2 2 1 5 2 9 C3 12 3 20 6 20 C8 20 8 13 10 13 C12 13 12 20 14 20 C17 20 17 12 18 9 C19 5 18 2 15 2 C13 2 12 3 10 3 C8 3 7 2 5 2 Z"/><path d="M6 6 L9 6"/></svg></span>
    <span class="service__label">Restorative<br>Dentistry</span>
  </div>
  <div class="abs service" style="left:43px;top:125px">
    <span class="service__icon"><svg width="20" height="18" viewBox="0 0 20 18" fill="none" stroke="var(--green)" stroke-width="1.2"><path d="M10 16 L2.5 8.5 A4.5 4.5 0 0 1 10 3 A4.5 4.5 0 0 1 17.5 8.5 Z"/></svg></span>
    <span class="service__label">Gentle &amp;<br>Comforting</span>
  </div>
  <div class="abs service" style="left:183px;top:125px">
    <span class="service__icon"><svg width="24" height="18" viewBox="0 0 24 18" fill="none" stroke="var(--green)" stroke-width="1.2"><path d="M12 2 C8 6 8 12 12 16 C16 12 16 6 12 2 Z"/><path d="M12 16 C8 16 4 13 3 8 C7 8 10 11 12 16 C14 11 17 8 21 8 C20 13 16 16 12 16 Z"/></svg></span>
    <span class="service__label">Calm<br>Environment</span>
  </div>
  <div class="abs service" style="left:43px;top:180px">
    <span class="service__icon"><svg width="22" height="22" viewBox="0 0 22 22" fill="none" stroke="var(--green)" stroke-width="1.2"><circle cx="11" cy="11" r="9"/><path d="M11 6 L11 11 L14 13"/></svg></span>
    <span class="service__label">Convenient<br>Scheduling</span>
  </div>
  <div class="abs service" style="left:183px;top:180px">
    <span class="service__icon"><svg width="26" height="16" viewBox="0 0 26 16" fill="none" stroke="var(--green)" stroke-width="1.2"><path d="M2 3 C2 13 6 13 7 8 C8 13 12 13 13 8 C14 13 18 13 19 8 C20 13 24 13 24 3"/><line x1="1" y1="7" x2="25" y2="7"/></svg></span>
    <span class="service__label">Orthodontic<br>Evaluations</span>
  </div>

  <div class="abs offer">
    <div class="offer__inner">
      <div class="offer__amount">$50<small>OFF</small></div>
      <div class="offer__line">YOUR CHILD’S FIRST VISIT!</div>
      <div class="offer__note">MENTION THIS CARD.</div>
    </div>
  </div>
  <div class="abs offer__notch">
    <svg width="14" height="12" viewBox="0 0 20 18"><path d="M10 17 L2 9 A5 5 0 0 1 10 2.5 A5 5 0 0 1 18 9 Z" fill="var(--green)"/></svg>
  </div>

  <ul class="abs contact">
    <li><svg width="12" height="15" viewBox="0 0 12 15"><path d="M6 14 C2 9 1 7 1 5 A5 5 0 0 1 11 5 C11 7 10 9 6 14 Z" fill="var(--green)"/><circle cx="6" cy="5" r="1.8" fill="#fff"/></svg><span>48 Linden Lane, Suite 200<span class="sep">|</span>Riverton, SC 29000</span></li>
    <li><svg width="13" height="13" viewBox="0 0 13 13"><path d="M2 1 L4.5 1 L5.5 4 L4 5.2 C4.8 7 6 8.2 7.8 9 L9 7.5 L12 8.5 L12 11 C12 12 11 12.5 10 12.3 C5.5 11.5 1.5 7.5 0.7 3 C0.5 2 1 1 2 1 Z" fill="var(--green)"/></svg><span>(555) 014-2290</span></li>
    <li><svg width="13" height="13" viewBox="0 0 13 13" fill="none" stroke="var(--green)" stroke-width="1.3"><circle cx="6.5" cy="6.5" r="5.6"/><ellipse cx="6.5" cy="6.5" rx="2.4" ry="5.6"/><line x1="1" y1="6.5" x2="12" y2="6.5"/></svg><span>maplegrovedentistry.com</span></li>
    <li><svg width="13" height="13" viewBox="0 0 13 13"><rect x="0.5" y="0.5" width="12" height="12" rx="2" fill="var(--green)"/></svg><span>@maplegrovedentistry</span></li>
  </ul>

  <div class="abs rule-v"></div>
  <div class="abs rule-heart"><svg width="20" height="18" viewBox="0 0 20 18"><path d="M10 17 L2 9 A5 5 0 0 1 10 2.5 A5 5 0 0 1 18 9 Z" fill="var(--green-pale)"/></svg></div>

  <div class="abs stamp">PLACE<br>STAMP<br>HERE</div>

  <div class="abs address-line" style="top:221px"></div>
  <div class="abs address-line" style="top:260px"></div>
  <div class="abs address-line" style="top:299px"></div>
  <div class="abs address-line" style="top:338px"></div>
  <div class="abs address-line" style="top:377px"></div>
  <div class="abs address-line" style="top:416px"></div>
</section>

</body>
</html>
```